Design Brief for Website Redesign

Client Name: Velmora IT
Website: www.velmorait.com.au
Industry: Managed IT Services
Target Audience: Small to medium-sized businesses in Australia, requiring IT solutions, IT support, cloud services, and phone systems.

Project Overview
We are seeking a full redesign of the Velmora IT website to modernize its look, improve usability, and enhance user experience across devices. The goal is to create a professional, clean, and user-friendly website that reflects our expertise in IT services and appeals to our business clients.

Objectives
Modern Visual Identity: Create a fresh, modern design that aligns with Velmora IT's branding.

Improved User Experience: Simplify navigation, improve accessibility, and enhance mobile responsiveness.

Clear Calls to Action: Ensure CTAs are prominent and encourage user engagement.

Enhanced Trust & Credibility: Highlight testimonials, case studies, and industry credentials.

SEO Optimization: Ensure the site is optimized for search engines, including proper heading structures and metadata.
Design Style & Tone
Professional: Clean, modern, and polished to reflect our IT expertise.

Minimalist: Simple layouts, plenty of white space, and easy-to-read typography.

Tech-focused: Subtle tech-themed design elements that reinforce our brand as a leading IT service provider.

Colors: Use our existing brand colors, or propose a color scheme that complements the tech industry while maintaining a professional feel.

Typography: Clear, readable fonts that convey professionalism and trustworthiness.

Key Pages & Features
Home Page:

Hero section with a clear value proposition.

Highlight key services (IT support, cloud solutions, phone systems, etc.) with icons and brief descriptions.

Prominent CTAs (e.g., “Request a Quote,” “Book a Demo”).

Testimonials from satisfied clients.

Services Page:

Detailed breakdown of the services we offer (IT support, cloud services, phone systems, etc.).

Use of icons or illustrations to make the services visually engaging.

Clear CTAs to request quotes or book consultations.

About Us Page:

Information about our company history, mission, and team.

Highlight our certifications, partnerships, and industry expertise.

Case Studies/Testimonials Page:

Showcase client success stories and testimonials with visuals and brief case study summaries.

Include a trust-building section with logos of major clients or partners.

Contact Page:

Simple contact form for inquiries.

Integrated map with office location.

Social media links and phone number.

Blog/Resource Section:

Easy-to-navigate blog section for IT-related articles, tips, and industry news.

Clear categorization and tags for easy browsing.

Knowledge Base/Support Page:

Self-service area for clients to find articles, FAQs, and support guides.

Option to submit a support ticket.

Mobile Responsiveness:

Ensure the design is fully responsive, with no horizontal scrolling or misaligned content on mobile.

Functional Requirements
Fast Load Times: Optimize images, minimize unnecessary scripts, and ensure the site loads quickly on both desktop and mobile.

User-Friendly CMS: We need a CMS that is easy to update (preferably WordPress, but open to other suggestions).

SEO Best Practices: Structure the site with proper metadata, alt tags, and semantic HTML for better search engine optimization.

Security: Ensure the website follows security best practices (SSL, HTTPS).

Deliverables
Full website design (desktop and mobile versions).

Design mockups in Photoshop, Sketch, or Figma (whichever is preferred).

Working prototype (optional).

Final website files, including images and assets.

A style guide for ongoing consistency.

Industry/Entity Type

IT Managed Services

Number of Pages Required

3 page

Requirements
Must have
• EXCELLENT UX/UI

```html
<!DOCTYPE html>
<html lang="en">
<head>
<meta charset="utf-8">
<title>Velmora IT – Managed IT Services Sydney</title>
<link href="https://fonts.googleapis.com/css2?family=Poppins:wght@300;400;500;600;700&display=swap" rel="stylesheet">
<style>
:root{
  --bg:#0c0506;
  --bg-soft:#140809;
  --card:#1b0b0e;
  --card-line:#3a161d;
  --red:#e3133d;
  --red-deep:#7a0a1e;
  --white:#ffffff;
  --text:#d9cfd1;
  --muted:#9a8c8f;
  --field:#241216;
}
*{box-sizing:border-box;margin:0;padding:0}
html,body{width:1200px;height:3900px;overflow:hidden}
body{background:var(--bg);color:var(--text);font-family:"Poppins",sans-serif;font-size:13px;line-height:1.6}
a{color:inherit;text-decoration:none}
.wrap{width:960px;margin:0 auto;position:relative}
section{position:relative;overflow:hidden}
h1,h2,h3,h4{color:var(--white);font-weight:700;line-height:1.2}
.btn{display:inline-flex;align-items:center;gap:8px;height:38px;padding:0 22px;border-radius:20px;font-size:12px;font-weight:600}
.btn-red{background:var(--red);color:var(--white)}
.btn-white{background:var(--white);color:#1a0a0d}
.btn-ghost{color:var(--white)}
.eyebrow{color:var(--red);font-size:12px;font-weight:600;margin-bottom:6px}
.center{text-align:center}

/* nav */
.nav{height:80px;display:flex;align-items:center;justify-content:space-between}
.brand{font-size:22px;font-weight:700;color:var(--white);display:flex;align-items:center;gap:8px}
.brand-dot{width:10px;height:10px;background:var(--red)}
.nav-links{display:flex;gap:30px;font-size:12px;color:var(--white)}
.nav-links span::after{content:" ▾";font-size:9px;color:var(--muted)}
.nav-links span.plain::after{content:""}

/* hero */
.hero{height:420px;text-align:center}
.hero-glow{position:absolute;left:0;right:0;top:180px;height:220px;background:radial-gradient(ellipse 60% 45% at 55% 55%,rgba(227,19,61,.55),rgba(120,10,30,.25) 50%,transparent 75%)}
.hero h1{font-size:44px;padding-top:60px;position:relative}
.hero p{font-size:16px;color:var(--white);margin-top:18px;position:relative}
.hero-ctas{display:flex;justify-content:center;gap:16px;margin-top:30px;position:relative}
.scroll-cue{position:relative;margin:48px auto 0;width:18px;height:28px;border:2px solid var(--muted);border-radius:10px}
.scroll-cue::after{content:"";position:absolute;left:6px;top:5px;width:2px;height:6px;background:var(--muted)}

/* partners */
.partners{height:100px;display:flex;align-items:center}
.partner-row{display:flex;justify-content:space-between;width:960px;margin:0 auto}
.partner-badge{width:96px;height:26px;border-radius:4px;background:#3b2b2e}

/* services */
.services{height:530px;padding-top:80px}
.services h2{font-size:30px}
.services .lead{width:720px;margin:14px auto 0;font-size:11px;color:var(--muted)}
.svc-grid{display:grid;grid-template-columns:repeat(3,1fr);gap:22px;margin-top:30px}
.svc-card{background:linear-gradient(160deg,var(--card),#120709);border:1px solid var(--card-line);border-radius:10px;height:200px;padding:26px 22px;text-align:left;display:flex;flex-direction:column;justify-content:flex-end}
.svc-icon{width:30px;height:30px;border-radius:6px;background:var(--red);display:flex;align-items:center;justify-content:center;margin-bottom:auto}
.svc-card h3{font-size:16px;margin-bottom:6px}
.svc-card p{font-size:11px;color:var(--muted)}
.svc-card .more{font-size:11px;color:var(--white);margin-top:10px}
.svc-ctas{display:flex;justify-content:center;gap:16px;margin-top:30px}

/* about */
.about{height:430px;padding-top:30px}
.about .wrap{display:grid;grid-template-columns:440px 440px;justify-content:space-between;align-items:start}
.about h2{font-size:30px;margin-bottom:16px}
.about p{font-size:11px;color:var(--muted);margin-bottom:10px}
.stats{display:flex;gap:50px;margin:16px 0 24px}
.stat b{display:block;font-size:36px;color:var(--white);font-weight:600;line-height:1.1}
.stat small{font-size:10px;color:var(--muted);display:block;width:110px}
.photo{border-radius:10px}
.about .photo{height:340px;background:linear-gradient(180deg,#0d1a2e 0%,#1a2b45 45%,#3a3a4a 70%,#12151f 100%)}

/* case study */
.case{height:450px}
.case h2{font-size:28px;margin-bottom:26px}
.case-grid{display:grid;grid-template-columns:380px 550px;justify-content:space-between}
.case .photo{height:240px;background:linear-gradient(135deg,#1c2a4a,#0b1222 60%,#2a0d14)}
.case-left .btn{margin-top:30px}
.case-right h3{font-size:18px;margin-bottom:8px}
.case-right p{font-size:11px;color:var(--muted);margin-bottom:8px}
.case-stats{display:grid;grid-template-columns:repeat(4,1fr);background:linear-gradient(90deg,var(--red-deep),var(--red));border-radius:8px 8px 0 0;padding:14px 18px;margin-top:10px}
.case-stats b{display:block;color:var(--white);font-size:18px;line-height:1.2}
.case-stats small{font-size:10px;color:#f5d5dc}
.case-quote{background:#3a0c16;border-radius:0 0 8px 8px;padding:14px 18px;position:relative}
.case-quote h4{font-size:12px;margin-bottom:4px}
.case-quote p{font-size:10px;color:#e6cdd2;margin:0;width:460px}
.case-quote .qm{position:absolute;right:18px;top:14px;font-size:44px;line-height:1;color:var(--red);font-weight:700}

/* testimonials */
.testi{height:430px;padding-top:40px}
.testi .wrap{display:grid;grid-template-columns:380px 540px;justify-content:space-between}
.testi h2{font-size:30px;margin-bottom:14px}
.testi p.lead{font-size:11px;color:var(--muted);margin-bottom:26px}
.review-cols{display:grid;grid-template-columns:1fr 1fr;gap:18px}
.review-col{display:flex;flex-direction:column;gap:18px}
.review-col.offset{margin-top:-20px}
.review{background:var(--card);border:1px solid var(--card-line);border-radius:10px;padding:18px}
.review.fade{opacity:.45}
.stars{color:var(--red);font-size:12px;letter-spacing:2px}
.review p{font-size:10px;color:var(--muted);margin:8px 0 12px}
.reviewer{display:flex;align-items:center;gap:10px}
.avatar{width:28px;height:28px;border-radius:50%;background:#4a2a30}
.reviewer b{display:block;color:var(--white);font-size:11px;font-weight:500;line-height:1.2}
.reviewer small{font-size:9px;color:var(--muted)}

/* cta banner */
.cta{height:300px;padding-top:40px}
.cta-box{height:240px;border-radius:12px;border:1px solid var(--card-line);background:linear-gradient(100deg,#5a0a1a 0%,#2a070e 35%,#140709 60%,#1a080b 100%);text-align:center;padding-top:62px;position:relative;overflow:hidden}
.cta-box::before{content:"";position:absolute;left:-60px;top:-40px;width:360px;height:320px;background:radial-gradient(ellipse at 30% 60%,rgba(227,19,61,.6),transparent 65%)}
.cta-box h2{font-size:30px;position:relative}
.cta-box p{font-size:13px;color:var(--white);margin:10px 0 22px;position:relative}
.cta-box .btn{position:relative}

/* resources */
.resources{height:510px;padding-top:40px}
.resources h2{font-size:30px;margin-bottom:30px}
.post-grid{display:grid;grid-template-columns:repeat(3,1fr);gap:22px}
.post{background:var(--card);border:1px solid var(--card-line);border-radius:10px;overflow:hidden;text-align:left}
.post .photo{height:150px;border-radius:0}
.post:nth-child(1) .photo{background:linear-gradient(135deg,#2a3a55,#141c2c)}
.post:nth-child(2) .photo{background:linear-gradient(135deg,#1c4a78,#0d1f3a)}
.post:nth-child(3) .photo{background:linear-gradient(135deg,#2a6aa0,#0b1a30)}
.post-body{padding:14px 16px 18px}
.post-meta{display:flex;gap:10px;align-items:center;font-size:9px;color:var(--muted)}
.tag{background:#3a1a20;color:var(--white);padding:2px 8px;border-radius:8px}
.post h3{font-size:14px;margin:10px 0 6px}
.post p{font-size:10px;color:var(--muted)}
.post .more{font-size:10px;color:var(--white);margin-top:8px;display:block}
.resources .btn{margin-top:28px}

/* contact */
.contact{height:390px;padding-top:10px}
.contact .wrap{display:grid;grid-template-columns:360px 540px;justify-content:space-between}
.contact h2{font-size:30px;margin-bottom:12px}
.contact-left h4{font-size:13px;font-weight:500;margin-bottom:10px}
.contact-left p{font-size:11px;color:var(--muted);margin-bottom:8px}
.form h3{font-size:14px;margin-bottom:10px}
.field-row{display:grid;grid-template-columns:1fr 1fr;gap:14px;margin-bottom:10px}
.field label{display:block;font-size:10px;color:var(--muted);margin-bottom:4px}
.field div{height:30px;background:var(--field);border-radius:4px}
.form .q{font-size:10px;color:var(--muted);margin:6px 0 8px}
.checks{display:grid;grid-template-columns:repeat(3,1fr);gap:8px 14px;font-size:10px;color:var(--text)}
.checks span{display:flex;align-items:center;gap:6px}
.checks span::before{content:"";width:10px;height:10px;border:1px solid var(--muted);border-radius:2px;flex:none}
.form .btn{margin:18px auto 0;display:flex;width:max-content}

/* footer */
.footer{height:280px;background:#080304;border-top:1px solid #1e0c10}
.footer .wrap{display:grid;grid-template-columns:200px 1fr 200px;padding-top:60px}
.foot-links{display:flex;flex-direction:column;gap:14px;font-size:11px;color:var(--white)}
.foot-mid{text-align:center}
.foot-mid .brand{justify-content:center;margin-bottom:14px}
.foot-mid p{font-size:10px;color:var(--muted);width:360px;margin:0 auto 6px}
.foot-social{display:flex;flex-direction:column;gap:18px;align-items:flex-end;font-size:11px;color:var(--white)}
.foot-social span{display:flex;align-items:center;gap:10px}
.foot-social i{width:22px;height:22px;border-radius:50%;background:var(--red);display:block}
</style>
</head>
<body>

<header class="wrap nav">
  <div class="brand"><span class="brand-dot"></span>Velmora IT</div>
  <nav class="nav-links"><span>Services</span><span>Solutions</span><span class="plain">About Us</span><span>Resources</span><span class="plain">Blog</span><span class="plain">Contact Us</span></nav>
  <a class="btn btn-white" href="#">Book a Demo</a>
</header>

<section class="hero">
  <div class="hero-glow" role="img" aria-label="Glowing red wave of tech particles"></div>
  <h1>Empowering Your Business with<br>Smarter IT Solutions</h1>
  <p>Reliable IT Support, Cybersecurity, Cloud Solutions and More</p>
  <div class="hero-ctas">
    <a class="btn btn-white" href="#">Request a Quote</a>
    <a class="btn btn-ghost" href="#">Explore Services →</a>
  </div>
  <div class="scroll-cue"></div>
</section>

<section class="partners">
  <div class="partner-row">
    <span class="partner-badge"></span><span class="partner-badge"></span><span class="partner-badge"></span><span class="partner-badge"></span><span class="partner-badge"></span><span class="partner-badge"></span><span class="partner-badge"></span>
  </div>
</section>

<section class="services center">
  <div class="wrap">
    <h2>Our Services</h2>
    <p class="lead">From day-to-day support to long-term strategy, our team keeps your systems secure, fast and running. We tailor every plan to the way your business works, so you can focus on growth while we look after the technology behind it.</p>
    <div class="svc-grid">
      <article class="svc-card">
        <div class="svc-icon"><svg width="16" height="16" viewBox="0 0 16 16"><rect x="2" y="3" width="12" height="8" rx="1" fill="none" stroke="#fff" stroke-width="1.5"/><path d="M5 14h6" stroke="#fff" stroke-width="1.5"/></svg></div>
        <h3>IT Consulting &amp; Training</h3>
        <p>Expert advice and hands-on training to help your team get more from technology.</p>
        <span class="more">Learn More About IT Consulting →</span>
      </article>
      <article class="svc-card">
        <div class="svc-icon"><svg width="16" height="16" viewBox="0 0 16 16"><path d="M4 12h8a3 3 0 0 0 0-6 4 4 0 0 0-7.5 1A2.5 2.5 0 0 0 4 12z" fill="none" stroke="#fff" stroke-width="1.5"/></svg></div>
        <h3>Cloud Services</h3>
        <p>Secure, scalable cloud platforms that keep your data available anywhere.</p>
        <span class="more">Learn More About Cloud Services →</span>
      </article>
      <article class="svc-card">
        <div class="svc-icon"><svg width="16" height="16" viewBox="0 0 16 16"><rect x="5" y="2" width="6" height="12" rx="1" fill="none" stroke="#fff" stroke-width="1.5"/></svg></div>
        <h3>Mobile &amp; Web Development</h3>
        <p>Custom apps and websites built to support your customers and your staff.</p>
        <span class="more">Learn More About Web Development →</span>
      </article>
    </div>
    <div class="svc-ctas">
      <a class="btn btn-red" href="#">View All Services</a>
      <a class="btn btn-ghost" href="#">Request a Quote →</a>
    </div>
  </div>
</section>

<section class="about">
  <div class="wrap">
    <div>
      <h2>Your Managed IT Services<br>Provider in Sydney</h2>
      <p>We're a local team helping Sydney businesses stay connected, protected and productive with proactive IT support and clear advice.</p>
      <p>From a single office to multiple sites, we plan, manage and support the technology your people rely on every day.</p>
      <div class="stats">
        <div class="stat"><b>5Years</b><small>Supporting local businesses</small></div>
        <div class="stat"><b>4.8</b><small>Average client rating from reviews</small></div>
      </div>
      <a class="btn btn-red" href="#">Learn More About Us</a>
    </div>
    <div class="photo" role="img" aria-label="Sydney harbour at night with the Opera House lit up"></div>
  </div>
</section>

<section class="case">
  <div class="wrap">
    <p class="eyebrow">Case Studies</p>
    <h2>Lorem ipsum dolor sit amet, consetetur sadipscing dolor</h2>
    <div class="case-grid">
      <div class="case-left">
        <div class="photo" role="img" aria-label="Laptop showing a business dashboard beside a presenter"></div>
        <a class="btn btn-red" href="#">View all Case Studies</a>
      </div>
      <div class="case-right">
        <h3>Client's Name Goes Here</h3>
        <p>We moved this client's ageing servers to the cloud, tightened security and set up round-the-clock support across three offices.</p>
        <p>The result was fewer outages, faster onboarding for new staff and a clear monthly cost they can plan around.</p>
        <div class="case-stats">
          <div><b>000+</b><small>Lorem Ipsum</small></div>
          <div><b>000%</b><small>Lorem Ipsum</small></div>
          <div><b>00k</b><small>Lorem Ipsum</small></div>
          <div><b>Texas</b><small>Lorem Ipsum dolor</small></div>
        </div>
        <div class="case-quote">
          <span class="qm">”</span>
          <h4>Words from the Client</h4>
          <p>The team took the stress out of our move to the cloud. Everything was planned, tested and explained, and our staff barely noticed the switch. Support is quick, friendly and always on hand.</p>
        </div>
      </div>
    </div>
  </div>
</section>

<section class="testi">
  <div class="wrap">
    <div>
      <p class="eyebrow">Testimonials</p>
      <h2>What Our Clients<br>Have to Say About<br>Our Services</h2>
      <p class="lead">Businesses across Sydney trust us to keep their systems running. Here's what a few of them have to say about working with our team.</p>
      <a class="btn btn-red" href="#">View all Testimonials</a>
    </div>
    <div class="review-cols">
      <div class="review-col">
        <div class="review">
          <div class="stars">★★★★★</div>
          <p>Fast response times and genuine care. They fixed issues our last provider ignored for months.</p>
          <div class="reviewer"><span class="avatar"></span><div><b>Kate Moran</b><small>Practice Manager</small></div></div>
        </div>
        <div class="review fade">
          <div class="stars">★★★★★</div>
          <p>Our network has never been more reliable. Great people to deal with.</p>
          <div class="reviewer"><span class="avatar"></span><div><b>Ben Foster</b><small>Director</small></div></div>
        </div>
      </div>
      <div class="review-col offset">
        <div class="review fade">
          <div class="stars">★★★★★</div>
          <p>Clear advice, fair pricing and no jargon. Highly recommended.</p>
          <div class="reviewer"><span class="avatar"></span><div><b>Sam Lee</b><small>Owner</small></div></div>
        </div>
        <div class="review">
          <div class="stars">★★★★★</div>
          <p>The move to the cloud was smooth and our staff can now work from anywhere with ease.</p>
          <div class="reviewer"><span class="avatar"></span><div><b>Mia Clarke</b><small>Operations Lead</small></div></div>
        </div>
      </div>
    </div>
  </div>
</section>

<section class="cta">
  <div class="wrap">
    <div class="cta-box">
      <h2>Looking for IT Support in Sydney?</h2>
      <p>Explore Managed IT Support Services For Your Business</p>
      <a class="btn btn-red" href="#">Request a Quote</a>
    </div>
  </div>
</section>

<section class="resources center">
  <div class="wrap">
    <h2>Helpful Resources</h2>
    <div class="post-grid">
      <article class="post">
        <div class="photo" role="img" aria-label="Team working at laptops in an office"></div>
        <div class="post-body">
          <div class="post-meta"><span class="tag">Cybersecurity</span>5 Min Read</div>
          <h3>Lorem ipsum dolor sit amet, conse ame adipiscing elit</h3>
          <p>Simple steps to keep your staff and data safe from common threats.</p>
          <span class="more">Read Full Blog Post →</span>
        </div>
      </article>
      <article class="post">
        <div class="photo" role="img" aria-label="Person using a laptop with cloud graphics"></div>
        <div class="post-body">
          <div class="post-meta"><span class="tag">Cloud</span>5 Min Read</div>
          <h3>Lorem ipsum dolor sit amet, conse ame adipiscing elit</h3>
          <p>How moving to the cloud can cut costs and boost flexibility.</p>
          <span class="more">Read Full Blog Post →</span>
        </div>
      </article>
      <article class="post">
        <div class="photo" role="img" aria-label="Hand touching a glowing digital network interface"></div>
        <div class="post-body">
          <div class="post-meta"><span class="tag">IT Support</span>5 Min Read</div>
          <h3>Lorem ipsum dolor sit amet, conse ame adipiscing elit</h3>
          <p>Signs it's time to switch to a proactive managed IT partner.</p>
          <span class="more">Read Full Blog Post →</span>
        </div>
      </article>
    </div>
    <a class="btn btn-red" href="#">View all Resources</a>
  </div>
</section>

<section class="contact">
  <div class="wrap">
    <div class="contact-left">
      <h2>Looking for IT Support<br>in Sydney?</h2>
      <h4>Explore Managed IT Support Services For Your Business</h4>
      <p>Tell us a little about your business and what you need. Our team will get back to you within one business day with next steps.</p>
      <p>Prefer to talk? Give us a call and we'll be happy to help.</p>
    </div>
    <form class="form">
      <h3>Let's Talk</h3>
      <div class="field-row">
        <div class="field"><label>First Name</label><div></div></div>
        <div class="field"><label>Last Name</label><div></div></div>
      </div>
      <div class="field-row">
        <div class="field"><label>Email</label><div></div></div>
        <div class="field"><label>Phone</label><div></div></div>
      </div>
      <p class="q">How can we help?</p>
      <div class="checks">
        <span>Help Desk Support</span><span>Data Security</span><span>Network Management</span>
        <span>Internet Connection</span><span>IT Procurement</span><span>Cloud Services</span>
        <span>Team Chat Tools</span><span>Email &amp; Office Apps</span><span>Phone Systems</span>
        <span>Software Support</span><span>Virtual Desktops</span><span>Other</span>
      </div>
      <a class="btn btn-red" href="#">Submit Form</a>
    </form>
  </div>
</section>

<footer class="footer">
  <div class="wrap">
    <div class="foot-links"><a href="#">Services</a><a href="#">About Us</a><a href="#">Resources</a><a href="#">Request a Quote</a></div>
    <div class="foot-mid">
      <div class="brand"><span class="brand-dot"></span>Velmora IT</div>
      <p>Velmora IT's team delivers managed IT, cloud and security services to businesses across Sydney.</p>
      <p>www.velmorait.com.au</p>
      <p>© 2025 Velmora IT. All rights reserved.</p>
    </div>
    <div class="foot-social"><span>Linkora <i></i></span><span>Chirpnet <i></i></span><span>Workwire <i></i></span></div>
  </div>
</footer>

</body>
</html>
```